Marlow Bridge needs a brochure review

We are a company operating in more than 10 countries that, since 1972, has the ambitious and innovative objective to stimulate foreign language learning by discovering different countries and cultures, through training courses tailored to individual needs
We need a layout review of our brochure in order to make the content clearer, immediate and appealing and, at the same time, make the layout more modern and young.
The pages we need are: the cover and pages 3, 5, 7, 20, 21, 22, 23, 34, 36, 37. You will find our actual brochure pdf as attachment

Target Market(s)

Students and families, business

Industry/Entity Type

It Company

Requirements
Must have
• The same written information as the actual one.
• Blue and green colours.
• The cover must be simple, elegant and clean but new and effective. In addition to the cover the pages you should review are number :2, 3, 4, 5, 6, 7. Feel free to use new background, images and new layout for the text.

```html
<!DOCTYPE html>
<html lang="it">
<head>
<meta charset="utf-8">
<title>Marlow Bridge – Vacanze Studio 2017</title>
<link href="https://fonts.googleapis.com/css2?family=Montserrat:wght@300;400;600;800&family=Indie+Flower&display=swap" rel="stylesheet">
<style>
  :root {
    --backdrop: #e4dcd9;
    --brand-blue: #2c5fa3;
    --band-blue: rgba(38, 100, 150, 0.92);
    --box-blue: rgba(40, 105, 160, 0.9);
    --accent-yellow: #f3e87c;
    --accent-pink: #e8566e;
    --panel-white: rgba(240, 244, 246, 0.72);
    --paper: #f7f7f5;
    --white: #ffffff;
  }
  * { margin: 0; padding: 0; box-sizing: border-box; }
  html, body {
    width: 1200px; height: 1200px; overflow: hidden;
    background: var(--backdrop);
    font-family: "Montserrat", sans-serif;
  }
  .cover {
    position: absolute; left: 197px; top: 30px;
    width: 806px; height: 1140px;
    overflow: hidden; background: var(--paper);
  }
  .cover-photo {
    position: absolute; inset: 0 0 70px 0;
    background:
      radial-gradient(ellipse at 70% 45%, #e9b893 0%, rgba(233,184,147,0) 45%),
      radial-gradient(ellipse at 30% 80%, #d9a07f 0%, rgba(217,160,127,0) 40%),
      linear-gradient(160deg, #7fb3c8 0%, #b7c9c6 35%, #d7b69a 60%, #6f8f9c 100%);
  }
  .edge-strip {
    position: absolute; left: 0; top: 0; width: 14px; height: 560px;
    background: #5fa6b8;
  }
  .intro-panel {
    position: absolute; left: 14px; top: 80px; width: 340px; height: 420px;
    background: var(--panel-white);
    padding: 42px 20px 0 36px;
  }
  .brand {
    display: flex; align-items: center; gap: 10px;
    font-weight: 800; font-size: 30px; color: var(--brand-blue);
    letter-spacing: -0.5px; margin-bottom: 36px; white-space: nowrap;
  }
  .brand-dot { width: 12px; height: 12px; border-radius: 50%; background: var(--accent-pink); flex: none; }
  .info-label { font-size: 21px; color: var(--brand-blue); letter-spacing: 1px; font-weight: 400; }
  .info-list { font-size: 21px; color: var(--accent-pink); line-height: 1.3; margin-bottom: 14px; font-weight: 400; }
  .offer-box {
    position: absolute; right: 0; top: 0; width: 350px; height: 200px;
    background: var(--box-blue);
    clip-path: polygon(0 0, 100% 0, 100% 100%, 0 88%);
    padding: 42px 30px 0 60px;
    font-size: 23px; line-height: 1.2; letter-spacing: 1px; font-weight: 300;
  }
  .offer-box .white { color: var(--white); }
  .offer-box .yellow { color: var(--accent-yellow); }
  .title-band {
    position: absolute; left: 0; top: 740px; width: 100%; height: 300px;
    background: var(--band-blue);
    padding: 34px 40px 0 40px;
  }
  .title-main {
    font-weight: 300; font-size: 66px; color: var(--white);
    letter-spacing: 1px; line-height: 1; white-space: nowrap;
  }
  .title-sub {
    display: flex; justify-content: space-between; margin-top: 18px;
    font-size: 19px; color: var(--accent-yellow); letter-spacing: 1px; white-space: nowrap;
  }
  .tagline {
    font-family: "Indie Flower", cursive;
    font-size: 58px; line-height: 1.2; color: var(--white);
    margin-top: 20px; padding-left: 150px; white-space: nowrap;
  }
</style>
</head>
<body>
  <main class="cover">
    <div class="cover-photo" role="img" aria-label="Foto di gruppo di ragazzi sorridenti con occhiali da sole che si scattano un selfie"></div>
    <div class="edge-strip"></div>

    <section class="intro-panel">
      <div class="brand"><span class="brand-dot"></span>Marlow Bridge</div>
      <p class="info-label">DESTINAZIONI:</p>
      <p class="info-list">Irlanda, Gran Bretagna<br>Stati Uniti, Malta,</p>
      <p class="info-label">PROGRAMMI:</p>
      <p class="info-list">Rugby, Calcio, Surf<br>Equitazione, Danza</p>
    </section>

    <aside class="offer-box">
      <span class="white">PREZZI<br>BLOCCATI</span><br>
      <span class="yellow">LIBERI DI<br>RIPENSARCI</span>
    </aside>

    <section class="title-band">
      <h1 class="title-main">Vacanze Studio 2017</h1>
      <div class="title-sub">
        <span>DAI 10 AI 18 ANNI</span>
        <span>DI GRUPPO CON ACCOMPAGNATORE</span>
      </div>
      <p class="tagline">L’estate che sogni</p>
    </section>
  </main>
</body>
</html>
```